Business Card for Health Food Store

I need a business card for a health food store that includes the following information.

=========
FRONT
=========

***White background***

Fernwell Market (logo)
Supplements - Health Foods - Remedies

2417 Larkwood Ave.
Alder Creek, CA 95999
(corner of Dunmore St.)

707-314-2296

FernwellMarket.example
FernwellLiving@mailbox.example

On the right side of the front of the card, use a circle type seal with 25 large in the middle. Put the dates below it.
"Celebrating 25 Years"
1997 - 2022

*DO NOT USE A PERSON'S NAME ON THE CARD*

==========
BACK
==========

***Green background***

Full logo in white along with the social logos and handles.

FB Logo / FernwellMarketShop
IG Logo / FernwellMarketShop
Twitter Logo / VisitFernwellMarket

When done I'll need the file in PSD and AI.

Target Market(s)

Surrounding local community

Industry/Entity Type

Retail Health Food Store

Contact Information for Business Card

See brief

Requirements
Must have
• Must be double-sided

```html
<!DOCTYPE html>
<html lang="en">
<head>
<meta charset="utf-8">
<title>Fernwell Market – Business Card</title>
<link rel="stylesheet" href="https://fonts.googleapis.com/css2?family=Outfit:wght@600;700;800&family=Barlow+Condensed:wght@600&family=Noto+Sans:wght@400&display=swap">
<style>
  :root{
    --green:#4fb848;
    --white:#ffffff;
    --ink:#111111;
    --stage:#3d3a3b;
    --text:#1d1d1d;
  }
  *{box-sizing:border-box;margin:0;padding:0}
  html,body{width:1200px;height:1200px;overflow:hidden;background:var(--stage)}
  .canvas{position:relative;width:1200px;height:1200px}

  .card{position:absolute;left:130px;width:940px;height:526px;overflow:hidden}
  .card--back{top:50px;background:var(--green)}
  .card--front{top:624px;background:var(--white)}

  /* back */
  .back-brand{position:absolute;left:0;right:0;top:210px;text-align:center;color:var(--white)}
  .back-brand .brand-name{font-family:"Outfit",sans-serif;font-weight:700;font-size:50px;line-height:1;letter-spacing:.3px}
  .back-brand .brand-tagline{font-family:"Barlow Condensed",sans-serif;font-weight:600;font-size:18.5px;letter-spacing:1.6px;margin-top:8px}
  .social-list{position:absolute;left:0;right:0;top:438px;display:flex;justify-content:center;gap:30px;list-style:none}
  .social-item{display:flex;align-items:center;gap:9px;font-family:"Noto Sans",sans-serif;font-size:24px;color:var(--white)}
  .social-dot{width:20px;height:20px;border-radius:50%;background:var(--white);flex:none}

  /* front */
  .front-stripe{position:absolute;left:0;top:0;width:38px;height:100%;background:var(--green)}
  .front-brand{position:absolute;left:109px;top:150px}
  .front-brand .brand-name{font-family:"Outfit",sans-serif;font-weight:700;font-size:47px;line-height:1;color:var(--ink)}
  .front-brand .brand-tagline{font-family:"Barlow Condensed",sans-serif;font-weight:600;font-size:17px;letter-spacing:1.3px;color:var(--green);margin-top:6px}
  .contact-list{list-style:none}
  .contact-row{position:absolute;left:109px;display:flex;align-items:flex-start;gap:19px;font-family:"Noto Sans",sans-serif;font-size:26px;line-height:34px;color:var(--text)}
  .contact-row--address{top:252px}
  .contact-row--phone{top:335px}
  .contact-row--web{top:392px}
  .contact-row--mail{top:451px}
  .contact-icon{width:44px;height:44px;flex:none;margin-top:-3px}

  .anniversary-seal{position:absolute;left:590px;top:110px;width:290px;height:290px;border-radius:50%;background:var(--green);display:flex;flex-direction:column;align-items:center;justify-content:center;color:var(--white);text-align:center}
  .anniversary-seal::before{content:"";position:absolute;inset:10px;border-radius:50%;border:2px solid rgba(255,255,255,.75)}
  .seal-label{font-family:"Barlow Condensed",sans-serif;font-weight:600;font-size:20px;letter-spacing:3px}
  .seal-number{font-family:"Outfit",sans-serif;font-weight:800;font-size:110px;line-height:.95}
  .seal-unit{font-family:"Barlow Condensed",sans-serif;font-weight:600;font-size:26px;letter-spacing:6px;margin-top:-2px}
  .seal-dates{font-family:"Outfit",sans-serif;font-weight:700;font-size:22px;margin-top:6px}
</style>
</head>
<body>
<main class="canvas">

  <section class="card card--back" aria-label="Business card back">
    <div class="back-brand">
      <div class="brand-name">Fernwell Market</div>
      <div class="brand-tagline">SUPPLEMENTS • HEALTH FOODS • REMEDIES</div>
    </div>
    <ul class="social-list">
      <li class="social-item"><span class="social-dot"></span>FernwellMarketShop</li>
      <li class="social-item"><span class="social-dot"></span>FernwellMarketShop</li>
      <li class="social-item"><span class="social-dot"></span>VisitFernwellMarket</li>
    </ul>
  </section>

  <section class="card card--front" aria-label="Business card front">
    <div class="front-stripe"></div>
    <div class="front-brand">
      <div class="brand-name">Fernwell Market</div>
      <div class="brand-tagline">SUPPLEMENTS • HEALTH FOODS • REMEDIES</div>
    </div>

    <ul class="contact-list">
      <li class="contact-row contact-row--address">
        <svg class="contact-icon" viewBox="0 0 44 44" aria-hidden="true">
          <rect width="44" height="44" fill="#4fb848"/>
          <circle cx="22" cy="22" r="15" fill="none" stroke="#fff" stroke-width="2"/>
          <path d="M22 31c-4-5-6-8-6-11a6 6 0 0 1 12 0c0 3-2 6-6 11z" fill="none" stroke="#fff" stroke-width="2"/>
          <circle cx="22" cy="20" r="2" fill="#fff"/>
        </svg>
        <span>2417 Larkwood Ave.<br>Alder Creek, CA 95999</span>
      </li>
      <li class="contact-row contact-row--phone">
        <svg class="contact-icon" viewBox="0 0 44 44" aria-hidden="true">
          <rect width="44" height="44" fill="#4fb848"/>
          <circle cx="22" cy="22" r="15" fill="none" stroke="#fff" stroke-width="2"/>
          <path d="M16 15l3-1 2 4-2 2c1 2 3 4 5 5l2-2 4 2-1 3c-7 0-13-6-13-13z" fill="none" stroke="#fff" stroke-width="1.8" stroke-linejoin="round"/>
        </svg>
        <span>707-314-2296</span>
      </li>
      <li class="contact-row contact-row--web">
        <svg class="contact-icon" viewBox="0 0 44 44" aria-hidden="true">
          <rect width="44" height="44" fill="#4fb848"/>
          <circle cx="22" cy="22" r="15" fill="none" stroke="#fff" stroke-width="2"/>
          <circle cx="22" cy="22" r="8.5" fill="none" stroke="#fff" stroke-width="1.6"/>
          <ellipse cx="22" cy="22" rx="3.5" ry="8.5" fill="none" stroke="#fff" stroke-width="1.4"/>
          <path d="M13.5 22h17M15 18h14M15 26h14" stroke="#fff" stroke-width="1.2"/>
        </svg>
        <span>FernwellMarket.example</span>
      </li>
      <li class="contact-row contact-row--mail">
        <svg class="contact-icon" viewBox="0 0 44 44" aria-hidden="true">
          <rect width="44" height="44" fill="#4fb848"/>
          <circle cx="22" cy="22" r="15" fill="none" stroke="#fff" stroke-width="2"/>
          <rect x="14" y="16" width="16" height="12" fill="none" stroke="#fff" stroke-width="1.6"/>
          <path d="M14 16l8 7 8-7" fill="none" stroke="#fff" stroke-width="1.6"/>
        </svg>
        <span>FernwellLiving@mailbox.example</span>
      </li>
    </ul>

    <div class="anniversary-seal" aria-label="Celebrating 25 years, 1997 to 2022">
      <div class="seal-label">CELEBRATING</div>
      <div class="seal-number">25</div>
      <div class="seal-unit">YEARS</div>
      <div class="seal-dates">1997 – 2022</div>
    </div>
  </section>

</main>
</body>
</html>
```